Expo Program Guide Design and Logo for Lantern Grove Gatherings

First, we are looking for a new logo for "Lantern Grove Gatherings" similar in feel to our other brands, Harvest Kite Fest and Bright Path Showcase. Attached is a graphic showing the three current logos.

Second we are looking for a new overall layout for our holistic living expo program guides that apply this new logo. Each 16-24 page guide has the following sections that need to have templates created that carry out the same look/feel.

a) front and back covers (similar in feel to the Denver Guide attached page 1 or Chicago page 1)
b) Welcome page (similar to the Chicago Guide attached page 3)
c) Expo lecture overview page (similar in feel to the Chicago Guide attached page 7, should only allow for 4 presentation rooms and be vertical to the page.)
d) Left detail page of presentations (similar in feel to the Chicago Guide attached page 34)
e) Right detail page of presentations (similar in feel to the Chicago Guide attached page 35)
f) Detail page for exhibitors (similar in feel to the Chicago Guide attached page 24)
g) Detail page for featured presenters (similar in feel to the Chicago Guide attached page 12)
f) Detail page for secondary featured presenters (similar in feel to the Chicago Guide attached page 15)

Target Market(s)

Casual female 25-54 with interest in holistic subjects

Requirements
Must have
• Logo should have horizontal aspect ratio.

Although samples may be in AI, PSD or PDF, we must have the templates in InDesign native files at the conclusion of the project for all pages of the guide.

Final logo should be vector based.

```html
<!DOCTYPE html>
<html lang="en">
<head>
<meta charset="utf-8">
<title>Lantern Grove Gatherings – Expo Program Guide</title>
<link rel="stylesheet" href="https://fonts.googleapis.com/css2?family=Righteous&family=Open+Sans:wght@400;600;700;800&display=swap">
<style>
:root{
  --ink:#4a4a4a;
  --grey:#6f6f6f;
  --plum:#8a2b6d;
  --magenta:#c2407f;
  --coral:#e8846d;
  --teal:#6cc4c9;
  --green:#5cb87f;
  --green-dark:#3f9c64;
  --yellow:#f5d21c;
  --sky:#9ec9e6;
  --sea:#6ea9cf;
  --sand:#d9c2a3;
  --paper:#ffffff;
  --display:'Righteous',sans-serif;
  --body:'Open Sans',sans-serif;
}
*{box-sizing:border-box;margin:0;padding:0}
html,body{width:868px;height:1200px;overflow:hidden;background:var(--paper)}
body{position:relative;font-family:var(--body);color:var(--ink)}
.board{position:relative;width:868px;height:1200px}

/* brand lockup */
.brand{position:absolute;left:0;right:0;top:52px;text-align:center}
.brand-mark{display:inline-block;width:22px;height:22px;border-radius:50%;background:var(--teal);margin-bottom:8px}
.brand-name{font-family:var(--display);font-size:36px;color:var(--grey);letter-spacing:1px;line-height:1}
.brand-sub{font-family:var(--display);font-size:22px;color:#8a8a8a;margin-top:6px;letter-spacing:2px}

.page{position:absolute;overflow:hidden;background:var(--paper);box-shadow:0 0 0 1px #e4e4e4}
.cover{left:32px;top:176px;width:374px;height:470px}
.welcome{left:428px;top:176px;width:374px;height:470px}
.program{left:32px;top:688px;width:374px;height:494px}
.exhibitors{left:428px;top:688px;width:374px;height:494px}

.photo{position:absolute}
.wave{position:absolute;left:0;width:100%}
.folio{position:absolute;right:12px;bottom:6px;font-size:5px;font-weight:700;color:#fff;letter-spacing:.3px}

/* cover */
.cover-scene{inset:0;background:linear-gradient(180deg,#7fb6de 0%,var(--sky) 40%,var(--sea) 58%,#c7d7dc 66%,var(--sand) 78%,#c9a987 100%)}
.cover-figure{left:20px;top:110px;width:230px;height:250px;background:radial-gradient(ellipse at 45% 45%,rgba(214,48,132,.85) 0%,rgba(214,48,132,.55) 45%,rgba(214,48,132,0) 72%)}
.cover-brand{position:absolute;left:0;right:0;top:46px;text-align:center;color:#fff;font-family:var(--display)}
.cover-brand .name{font-size:22px;letter-spacing:.5px}
.cover-brand .year{font-size:16px;margin-top:2px}
.event{position:absolute;left:204px;top:122px;color:var(--yellow);font-family:var(--display);line-height:1.05}
.event .city{font-size:20px}
.event .venue{font-size:8px;color:#fff}
.event .dates{font-size:15px}
.event .hours,.event .fee{font-size:8px;color:#fff}
.themes{position:absolute;right:22px;top:246px;text-align:right;font-family:var(--display);line-height:1}
.themes .a{font-size:20px;color:var(--yellow)}
.themes .b{font-size:20px;color:#fff}
.stats{position:absolute;left:24px;top:302px;font-family:var(--display);color:#fff;line-height:1.1}
.stats .big{font-size:15px}
.stats .mid{font-size:11px}
.speakers{position:absolute;left:40px;top:358px;display:flex;gap:30px}
.speaker{width:82px;text-align:left}
.speaker .portrait{width:56px;height:56px;border-radius:8px;border:2px solid #fff;background:linear-gradient(160deg,#e9d3c2,#b99a84)}
.speaker .role{font-family:var(--display);color:var(--yellow);font-size:6px;margin-top:3px}
.speaker .who{font-family:var(--display);color:var(--yellow);font-size:7.5px}
.speaker .topic{font-size:6px;font-style:italic;color:#fff;line-height:1.2}

/* welcome */
.welcome .head-title{position:absolute;right:26px;top:20px;font-family:var(--display);font-size:16px;color:#fff}
.bar{display:block;font-family:var(--display);color:#fff;font-size:9px;padding:1px 6px}
.bar.plum{background:linear-gradient(90deg,var(--plum),var(--magenta))}
.whats-in{position:absolute;left:0;top:62px;width:140px}
.thumbs{display:flex;gap:4px;padding:4px 0 0 4px}
.thumbs .photo{position:static;width:42px;height:42px}
.t1{background:linear-gradient(160deg,#a7d0ea,#d34c8c)}
.t2{background:linear-gradient(160deg,#eef3dc,#7fb56b)}
.t3{background:linear-gradient(160deg,#dfe8df,#40463f)}
.toc{list-style:none;padding:8px 6px 0 4px;font-size:5.2px;line-height:1.45}
.toc li{display:flex;justify-content:space-between;width:100px}
.credits{position:absolute;left:8px;top:272px;width:140px}
.mini-brand{font-family:var(--display);color:var(--grey);white-space:nowrap}
.mini-brand .name{font-size:9px;line-height:1.1;display:flex;align-items:center;gap:3px}
.mini-brand .dot{flex:none;width:6px;height:6px;border-radius:50%;background:var(--teal)}
.mini-brand .year{font-size:7px;line-height:1.2;padding-left:9px}
.staff{display:grid;grid-template-columns:62px 1fr;font-size:5px;line-height:1.5;margin:10px 0 0 2px}
.thanks{width:120px;font-size:5px;line-height:1.45;margin:8px 0 0 2px}
.greeting{position:absolute;left:160px;top:62px;width:200px}
.greeting h2{font-family:var(--body);font-weight:700;font-size:14px;color:var(--ink);margin-bottom:8px}
.greeting p{font-size:5.2px;line-height:1.45;margin-bottom:6px}
.volunteer{position:absolute;left:160px;top:272px;width:214px}
.volunteer .photo{position:static;width:90px;height:110px;float:left;margin:4px 6px 0 4px;background:linear-gradient(160deg,#d9c6b8,#8d5d4c 70%,#6f7d8e)}
.volunteer p{font-size:5.2px;line-height:1.45;padding-top:4px;margin-bottom:5px;padding-right:8px}

/* program */
.program .head-title{position:absolute;right:26px;top:22px;font-family:var(--display);font-size:12px;color:#fff}
.feature{position:absolute;left:14px;top:60px;width:346px}
.feature .photo{position:static;float:left;width:88px;height:84px;margin-right:10px;background:linear-gradient(160deg,#e8eef2,#9db3c8)}
.slot{font-size:5px;font-weight:700;color:var(--coral);text-transform:uppercase}
.speaker-name{font-weight:700;font-size:8px;color:var(--ink)}
.speaker-talk{font-size:5.5px;color:#9a9a9a;margin-bottom:3px}
.bio{font-size:4.8px;line-height:1.45;color:#555}
.sessions{position:absolute;left:0;top:156px;width:374px;display:grid;grid-template-columns:1fr 1fr;column-gap:8px}
.session{margin-bottom:10px}
.session .label{font-size:5px;font-weight:700;color:#fff;padding:2px 6px}
.label.coral{background:var(--coral)}
.label.teal{background:var(--teal)}
.session .body{padding:3px 8px 0 14px}
.session .row{display:flex;gap:6px;align-items:flex-start}
.session .face{flex:none;width:40px;height:46px;background:linear-gradient(160deg,#f0e2d6,#c4a08a)}
.left-col .label{margin-right:14px}
.right-col .label{margin-left:14px;text-align:right}
.right-col .body{padding:3px 14px 0 6px}

/* exhibitors */
.exhibitors .head-title{position:absolute;right:26px;top:22px;font-family:var(--display);font-size:13px;color:#fff}
.listing{position:absolute;left:28px;top:58px;width:318px;display:grid;grid-template-columns:repeat(3,1fr);column-gap:4px;row-gap:7px}
.entry .tag{display:flex;justify-content:space-between;background:var(--green);color:#fff;font-size:5.2px;font-weight:700;padding:1.5px 4px}
.entry p{font-size:4.8px;line-height:1.4;color:#555;padding:2px 4px 0}
</style>
</head>
<body>
<main class="board">

  <header class="brand">
    <span class="brand-mark"></span>
    <div class="brand-name">LANTERN GROVE GATHERINGS</div>
    <div class="brand-sub">EXPO 2013</div>
  </header>

  <!-- front cover -->
  <section class="page cover">
    <div class="photo cover-scene" role="img" aria-label="Beach at sunrise with a dancer trailing a pink scarf"></div>
    <div class="photo cover-figure" role="img" aria-label="Dancer in a flowing pink dress"></div>
    <div class="cover-brand">
      <div class="name">LANTERN GROVE GATHERINGS</div>
      <div class="year">EXPO 2013</div>
    </div>
    <div class="event">
      <div class="city">DENVER</div>
      <div class="venue">HARBOR HALL</div>
      <div class="dates">SEPT 6-8</div>
      <div class="hours">FRI 1-9, SAT 10-7, SUN 10-6</div>
      <div class="fee">ADMISSION $5</div>
    </div>
    <div class="themes">
      <div class="a">NATURAL HEALTH</div>
      <div class="b">PERSONAL GROWTH</div>
    </div>
    <div class="stats">
      <div class="big">220 EXHIBITORS</div>
      <div class="mid">80 HEALERS &amp; READERS</div>
      <div class="mid">65 FREE SEMINAIRS</div>
    </div>
    <div class="speakers">
      <div class="speaker">
        <div class="portrait" role="img" aria-label="Portrait of speaker Irena Calloway"></div>
        <div class="who">IRENA CALLOWAY</div>
        <div class="topic">Law of attraction</div>
      </div>
      <div class="speaker">
        <div class="portrait" role="img" aria-label="Portrait of keynote Tova Linden"></div>
        <div class="role">KEYNOTE</div>
        <div class="who">Tova Linden</div>
        <div class="topic">Recerfecon aute, nonsi csejdcdggx</div>
      </div>
      <div class="speaker">
        <div class="portrait" role="img" aria-label="Portrait of speaker Wendell Ashby"></div>
        <div class="who">WENDELL ASHBY</div>
        <div class="topic">Recerfecon aute, nonsi csejdcdggx Recerfecon aute</div>
      </div>
    </div>
  </section>

  <!-- welcome page -->
  <section class="page welcome">
    <svg class="wave" style="top:0" height="60" viewBox="0 0 374 60" preserveAspectRatio="none" aria-hidden="true">
      <path d="M0 0H374V40C300 58 220 30 150 40C90 48 40 44 0 36Z" fill="var(--plum)"/>
      <path d="M0 36C40 44 90 48 150 40C220 30 300 58 374 40V46C300 64 220 36 150 46C90 54 40 50 0 42Z" fill="var(--magenta)" opacity=".7"/>
    </svg>
    <div class="head-title">WELCOME</div>

    <div class="whats-in">
      <span class="bar plum">what's in</span>
      <div class="thumbs">
        <div class="photo t1" role="img" aria-label="Dancer with pink scarf on the beach"></div>
        <div class="photo t2" role="img" aria-label="Yoga pose in a green field"></div>
        <div class="photo t3" role="img" aria-label="Stacked spa stones"></div>
      </div>
      <ul class="toc">
        <li><span>WELCOME &amp; DIRECTIONS</span><span>3</span></li>
        <li><span>ORDERING TICKETS</span><span>5</span></li>
        <li><span>CONFERENCE SCHEDULE</span><span>6-8</span></li>
        <li><span>KEYNOTES</span><span>9-14</span></li>
        <li><span>WORKSHOPS</span><span>15-21</span></li>
        <li><span>EXHIBITORS &amp; FLOORPLAN</span><span>23-25</span></li>
        <li><span>YOGA DOME</span><span>27</span></li>
        <li><span>PANELS</span><span>28-29</span></li>
        <li><span>MUSIC STAGE</span><span>30</span></li>
        <li><span>FRIDAY LECTURES</span><span>32-35</span></li>
        <li><span>SATURDAY LECTURES</span><span>36-43</span></li>
        <li><span>SUNDAY LECTURES</span><span>44-45</span></li>
        <li><span>LONGEVITY PAVILION</span><span>46-47</span></li>
      </ul>
    </div>

    <div class="credits">
      <div class="mini-brand">
        <div class="name"><span class="dot"></span>LANTERN GROVE GATHERINGS</div>
        <div class="year">EXPO 2013</div>
      </div>
      <div class="staff">
        <span>Colin Ashgrove</span><span>Producer</span>
        <span>Priya Holloway</span><span>Producer</span>
        <span>Dale Fenwick</span><span>Producer</span>
        <span>Jess Barlow</span><span>Sales</span>
        <span>Owen Tasaki</span><span>Sales</span>
        <span>Nora Whitfield</span><span>Customer Support</span>
        <span>Samira Quill</span><span>Yoga Dome</span>
        <span>Greg Lomax</span><span>Public Relations</span>
        <span>Tessa Rowe</span><span>Program</span>
      </div>
      <p class="thanks">Special thanks to Ruth Kendal, Mara Voss, Ella Pruitt, Hal Benning, Iris Calder, Jude Marlow, and more!</p>
    </div>

    <article class="greeting">
      <h2>Hi everyone!</h2>
      <p>For many of us the name Bright Path Showcase takes us back to the early days of the holistic movement. Through the eighties and nineties these shows crossed the country and served as a home for a fresh world view that has since reached the globe. Many ideas, healing practices and lifestyles first seen here are now part of daily life, and we are proud to celebrate over thirty years together.</p>
      <p>At the expo we have done more than gather companies together. We have built a village of themed booths with their own stages, colours and designs, a dome for movement and yoga, and the largest lecture schedule yet, with more than 250 speakers.</p>
      <p>Sit back and enjoy the very best presenters from the region and across the country, including the author of this season's most loved book on life after healing.</p>
    </article>

    <aside class="volunteer">
      <span class="bar plum">volunteer at the expo</span>
      <div class="photo" role="img" aria-label="Smiling volunteer in a yoga stretch"></div>
      <p>In exchange for a 4-hour shift we offer a free weekend pass to the expo. You get to see the event from both sides and help the whole weekend run smoothly. We have specific areas of focus for your shift.</p>
      <p>If you would like to help in one of these areas, give Nora a call at 555-014-2286 and let us know your availability. Shifts run from 9AM-1PM on Saturday and Sunday, 12:30 PM-4:30 PM on Friday and 3:30-7:30 on Sunday.</p>
    </aside>

    <svg class="wave" style="bottom:0" height="50" viewBox="0 0 374 50" preserveAspectRatio="none" aria-hidden="true">
      <path d="M0 14C80 0 170 26 250 18C310 12 350 4 374 8V50H0Z" fill="var(--magenta)" opacity=".6"/>
      <path d="M0 22C80 8 170 34 250 26C310 20 350 12 374 16V50H0Z" fill="var(--plum)"/>
    </svg>
    <div class="folio">LANTERN GROVE GATHERINGS EXPO 2013 &nbsp;03</div>
  </section>

  <!-- saturday presentation page -->
  <section class="page program">
    <svg class="wave" style="top:0" height="58" viewBox="0 0 374 58" preserveAspectRatio="none" aria-hidden="true">
      <path d="M0 0H374V34C300 52 220 26 150 36C90 44 40 40 0 30Z" fill="var(--coral)"/>
      <path d="M0 30C40 40 90 44 150 36C220 26 300 52 374 34V42C300 60 220 34 150 44C90 52 40 48 0 38Z" fill="var(--teal)"/>
    </svg>
    <div class="head-title">SATURDAY PRESENTATION</div>

    <article class="feature">
      <div class="photo" role="img" aria-label="Portrait of featured presenter Dr Alden Marsh"></div>
      <div class="slot">Saturday 10 - Centre Room</div>
      <div class="speaker-name">Dr Alden Marsh</div>
      <div class="speaker-talk">Channeled Meditation Meditation</div>
      <p class="bio">Dr Owen Kessler, founder of Longevity Factors in Health, worked with island communities to design a whole food nutrition plan that draws on the world's longest living regions. He compared the daily habits of people there with the average modern lifestyle and built a wellness protocol called the Bright Path Blueprint.</p>
    </article>

    <div class="sessions">
      <div class="left-col">
        <div class="session">
          <div class="label coral">SATURDAY 10 AM - CENTRE ROOM</div>
          <div class="body">
            <div class="speaker-name">Dr Alden Marsh</div>
            <div class="speaker-talk">Channeled Meditation Meditation</div>
            <div class="row"><div class="face" role="img" aria-label="Presenter portrait"></div><p class="bio">Alden Marsh uses intuitive reading, spiritual channeling, bodywork and metaphysical healing as he guides each listener into a place of aliveness and ease. Join him as he presents a channeled healing meditation that supports everyone present in their own transformation. Alden travels widely sharing his unique style.</p></div>
          </div>
        </div>
        <div class="session">
          <div class="label teal">SATURDAY 11 AM - CENTRE ROOM</div>
          <div class="body">
            <div class="speaker-name">Dr Alden Marsh</div>
            <div class="speaker-talk">Channeled Meditation Meditation</div>
            <div class="row"><div class="face" role="img" aria-label="Presenter portrait"></div><p class="bio">Alden Marsh uses intuitive reading, spiritual channeling, bodywork and metaphysical healing as he guides each listener into a place of aliveness and ease. Join him as he presents a channeled healing meditation that supports everyone present in their own transformation. Alden travels widely sharing his unique style.</p></div>
          </div>
        </div>
        <div class="session">
          <div class="label coral">SATURDAY 12 AM - CENTRE ROOM</div>
          <div class="body">
            <div class="speaker-name">Dr Alden Marsh</div>
            <div class="speaker-talk">Channeled Meditation Meditation</div>
            <div class="row"><div class="face" role="img" aria-label="Presenter portrait"></div><p class="bio">Alden Marsh uses intuitive reading, spiritual channeling, bodywork and metaphysical healing as he guides each listener into a place of aliveness and ease. Join him as he presents a channeled healing meditation that supports everyone present in their own transformation. Alden travels widely sharing his unique style.</p></div>
          </div>
        </div>
      </div>
      <div class="right-col">
        <div class="session">
          <div class="label teal">SATURDAY 10 AM - CENTRE ROOM</div>
          <div class="body">
            <div class="speaker-name">Dr Alden Marsh</div>
            <div class="speaker-talk">Channeled Meditation Meditation</div>
            <div class="row"><p class="bio">Alden Marsh uses intuitive reading, spiritual channeling, bodywork and metaphysical healing as he guides each listener into a place of aliveness and ease. Join him as he presents a channeled healing meditation that supports everyone present in their own transformation. Alden travels widely sharing his unique style.</p><div class="face" role="img" aria-label="Presenter portrait"></div></div>
          </div>
        </div>
        <div class="session">
          <div class="label coral">SATURDAY 10 AM - CENTRE ROOM</div>
          <div class="body">
            <div class="speaker-name">Dr Alden Marsh</div>
            <div class="speaker-talk">Channeled Meditation Meditation</div>
            <div class="row"><p class="bio">Alden Marsh uses intuitive reading, spiritual channeling, bodywork and metaphysical healing as he guides each listener into a place of aliveness and ease. Join him as he presents a channeled healing meditation that supports everyone present in their own transformation. Alden travels widely sharing his unique style.</p><div class="face" role="img" aria-label="Presenter portrait"></div></div>
          </div>
        </div>
        <div class="session">
          <div class="label teal">SATURDAY 10 AM - CENTRE ROOM</div>
          <div class="body">
            <div class="speaker-name">Dr Alden Marsh</div>
            <div class="speaker-talk">Channeled Meditation Meditation</div>
            <div class="row"><p class="bio">Alden Marsh uses intuitive reading, spiritual channeling, bodywork and metaphysical healing as he guides each listener into a place of aliveness and ease. Join him as he presents a channeled healing meditation that supports everyone present in their own transformation. Alden travels widely sharing his unique style.</p><div class="face" role="img" aria-label="Presenter portrait"></div></div>
          </div>
        </div>
      </div>
    </div>

    <svg class="wave" style="bottom:0" height="46" viewBox="0 0 374 46" preserveAspectRatio="none" aria-hidden="true">
      <path d="M0 12C80 0 170 24 250 16C310 10 350 4 374 6V46H0Z" fill="var(--teal)"/>
      <path d="M0 20C80 8 170 32 250 24C310 18 350 12 374 14V46H0Z" fill="var(--coral)"/>
    </svg>
    <div class="folio">LANTERN GROVE GATHERINGS EXPO 2013 &nbsp;06</div>
  </section>

  <!-- exhibitors page -->
  <section class="page exhibitors">
    <svg class="wave" style="top:0" height="56" viewBox="0 0 374 56" preserveAspectRatio="none" aria-hidden="true">
      <path d="M0 0H374V34C300 50 220 24 150 34C90 42 40 38 0 28Z" fill="var(--green)"/>
      <path d="M0 28C40 38 90 42 150 34C220 24 300 50 374 34V40C300 56 220 30 150 40C90 48 40 44 0 34Z" fill="var(--teal)"/>
    </svg>
    <div class="head-title">EXHIBITORS</div>

    <div class="listing">
      <div class="entry"><div class="tag"><span>ALLU MERALLY</span><span>05</span></div><p>icipsum dest qui dolum<br>sum intinctur?</p></div>
      <div class="entry"><div class="tag"><span>LLU MERALLY</span><span>15</span></div><p>icipsum dest qui dolum<br>sum intinctur?</p></div>
      <div class="entry"><div class="tag"><span>LLU MERALLY</span><span>35</span></div><p>icipsum dest qui dolum<br>sum intinctur?</p></div>
      <div class="entry"><div class="tag"><span>ALLU MERALLY</span><span>05</span></div><p>icipsum dest qui dolum<br>sum intinctur?</p></div>
      <div class="entry"><div class="tag"><span>ALLU MERALLY</span><span>05</span></div><p>icipsum dest qui dolum<br>sum intinctur?</p></div>
      <div class="entry"><div class="tag"><span>ALLU MERALLY</span><span>05</span></div><p>icipsum dest qui dolum<br>sum intinctur?</p></div>
      <div class="entry"><div class="tag"><span>ALLU MERALLY</span><span>05</span></div><p>icipsum dest qui dolum<br>sum intinctur?</p></div>
      <div class="entry"><div class="tag"><span>ALLU MERALLY</span><span>05</span></div><p>icipsum dest qui dolum<br>sum intinctur?</p></div>
      <div class="entry"><div class="tag"><span>ALLU MERALLY</span><span>05</span></div><p>icipsum dest qui dolum<br>sum intinctur?</p></div>
      <div class="entry"><div class="tag"><span>ALLU MERALLY</span><span>05</span></div><p>icipsum dest qui dolum<br>sum intinctur?</p></div>
      <div class="entry"><div class="tag"><span>ALLU MERALLY</span><span>05</span></div><p>icipsum dest qui dolum<br>sum intinctur?</p></div>
      <div class="entry"><div class="tag"><span>ALLU MERALLY</span><span>05</span></div><p>icipsum dest qui dolum<br>sum intinctur?</p></div>
      <div class="entry"><div class="tag"><span>ALLU MERALLY</span><span>05</span></div><p>icipsum dest qui dolum<br>sum intinctur?</p></div>
      <div class="entry"><div class="tag"><span>ALLU MERALLY</span><span>05</span></div><p>icipsum dest qui dolum<br>sum intinctur?</p></div>
      <div class="entry"><div class="tag"><span>ALLU MERALLY</span><span>05</span></div><p>icipsum dest qui dolum<br>sum intinctur?</p></div>
      <div class="entry"><div class="tag"><span>ALLU MERALLY</span><span>05</span></div><p>icipsum dest qui dolum<br>sum intinctur?</p></div>
      <div class="entry"><div class="tag"><span>ALLU MERALLY</span><span>05</span></div><p>icipsum dest qui dolum<br>sum intinctur?</p></div>
      <div class="entry"><div class="tag"><span>ALLU MERALLY</span><span>05</span></div><p>icipsum dest qui dolum<br>sum intinctur?</p></div>
      <div class="entry"><div class="tag"><span>ALLU MERALLY</span><span>05</span></div><p>icipsum dest qui dolum<br>sum intinctur?</p></div>
      <div class="entry"><div class="tag"><span>ALLU MERALLY</span><span>05</span></div><p>icipsum dest qui dolum<br>sum intinctur?</p></div>
      <div class="entry"><div class="tag"><span>ALLU MERALLY</span><span>05</span></div><p>icipsum dest qui dolum<br>sum intinctur?</p></div>
      <div class="entry"><div class="tag"><span>ALLU MERALLY</span><span>05</span></div><p>icipsum dest qui dolum<br>sum intinctur?</p></div>
      <div class="entry"><div class="tag"><span>ALLU MERALLY</span><span>05</span></div><p>icipsum dest qui dolum<br>sum intinctur?</p></div>
      <div class="entry"><div class="tag"><span>ALLU MERALLY</span><span>05</span></div><p>icipsum dest qui dolum<br>sum intinctur?</p></div>
      <div class="entry"><div class="tag"><span>ALLU MERALLY</span><span>05</span></div><p>icipsum dest qui dolum<br>sum intinctur?</p></div>
      <div class="entry"><div class="tag"><span>ALLU MERALLY</span><span>05</span></div><p>icipsum dest qui dolum<br>sum intinctur?</p></div>
      <div class="entry"><div class="tag"><span>ALLU MERALLY</span><span>05</span></div><p>icipsum dest qui dolum<br>sum intinctur?</p></div>
      <div class="entry"><div class="tag"><span>ALLU MERALLY</span><span>05</span></div><p>icipsum dest qui dolum<br>sum intinctur?</p></div>
      <div class="entry"><div class="tag"><span>ALLU MERALLY</span><span>05</span></div><p>icipsum dest qui dolum<br>sum intinctur?</p></div>
      <div class="entry"><div class="tag"><span>ALLU MERALLY</span><span>05</span></div><p>icipsum dest qui dolum<br>sum intinctur?</p></div>
      <div class="entry"><div class="tag"><span>ALLU MERALLY</span><span>05</span></div><p>icipsum dest qui dolum<br>sum intinctur?</p></div>
      <div class="entry"><div class="tag"><span>ALLU MERALLY</span><span>05</span></div><p>icipsum dest qui dolum<br>sum intinctur?</p></div>
      <div class="entry"><div class="tag"><span>ALLU MERALLY</span><span>05</span></div><p>icipsum dest qui dolum<br>sum intinctur?</p></div>
    </div>

    <svg class="wave" style="bottom:0" height="44" viewBox="0 0 374 44" preserveAspectRatio="none" aria-hidden="true">
      <path d="M0 12C80 0 170 24 250 16C310 10 350 4 374 6V44H0Z" fill="var(--teal)"/>
      <path d="M0 20C80 8 170 32 250 24C310 18 350 12 374 14V44H0Z" fill="var(--green-dark)"/>
    </svg>
    <div class="folio">LANTERN GROVE GATHERINGS EXPO 2013 &nbsp;07</div>
  </section>

</main>
</body>
</html>
```